FotoVELTA buisnesscard

Hey :) I need a modern buisnesscard for my company FotoVELTA
It most have:
Dagligleder og Fotograf: Henrik Torvald Bjelland

Mob: +4791642058
Epost: post@fotovelta.no
Adresse: Bakkestien22, 6190 Fjordvik

Facbook and instagram logo with text FotoVELTA

FotoVELTA logo

It Company

```html
<!DOCTYPE html>
<html lang="no">
<head>
<meta charset="utf-8">
<title>FotoVELTA – visittkort</title>
<link rel="stylesheet" href="https://fonts.googleapis.com/css2?family=Exo+2:wght@500;700;800&display=swap">
<style>
  :root {
    --stage: #2a2626;
    --card-dark: #0d0d0d;
    --card-dark-edge: #1c1c1c;
    --card-light: #ffffff;
    --ink: #0a0a0a;
    --silver: #d9d9d9;
    --muted: #222222;
  }
  * { box-sizing: border-box; margin: 0; padding: 0; }
  html, body {
    width: 1200px; height: 901px; overflow: hidden;
    background: var(--stage);
    font-family: "Exo 2", Arial, sans-serif;
  }
  .stage {
    width: 1200px; height: 901px;
    display: flex; align-items: center; justify-content: center; gap: 40px;
  }
  .card {
    width: 540px; height: 309px; position: relative; overflow: hidden;
    box-shadow: 0 10px 30px rgba(0,0,0,.5);
  }
  .card--front {
    background: radial-gradient(ellipse at 50% 45%, var(--card-dark-edge), var(--card-dark) 75%);
    display: flex; align-items: center; justify-content: center;
  }
  .brand-front {
    display: flex; align-items: center; gap: 16px;
    color: var(--silver); font-weight: 800; font-size: 54px; letter-spacing: 1px;
  }
  .brand-front .mark { width: 46px; height: 46px; background: var(--silver); }
  .card--back { background: var(--card-light); color: var(--ink); }
  .brand-back {
    position: absolute; top: 24px; right: 34px;
    font-weight: 800; font-size: 34px; letter-spacing: .5px;
  }
  .holder {
    position: absolute; left: 0; top: 116px; bottom: 30px;
    display: flex;
  }
  .holder .bar { width: 26px; background: var(--ink); }
  .holder .info { padding: 6px 0 0 16px; }
  .name { font-weight: 700; font-size: 22px; line-height: 1.1; }
  .role { font-weight: 700; font-size: 14px; margin: 3px 0 12px; }
  .contact { list-style: none; font-size: 13px; font-weight: 500; color: var(--muted); }
  .contact li { display: flex; align-items: center; gap: 7px; line-height: 19px; }
  .contact svg { width: 11px; height: 11px; fill: var(--ink); flex: none; }
  .social .dot { width: 10px; height: 10px; border-radius: 50%; background: var(--ink); }
</style>
</head>
<body>
<main class="stage">
  <section class="card card--front" aria-label="Visittkort forside">
    <div class="brand-front"><span class="mark"></span>FotoVELTA</div>
  </section>

  <section class="card card--back" aria-label="Visittkort bakside">
    <div class="brand-back">FotoVELTA</div>
    <div class="holder">
      <div class="bar"></div>
      <div class="info">
        <p class="name">Henrik Torvald Bjelland</p>
        <p class="role">Dagligleder og Fotograf</p>
        <ul class="contact">
          <li><svg viewBox="0 0 24 24"><path d="M6.6 10.8a15.1 15.1 0 0 0 6.6 6.6l2.2-2.2a1 1 0 0 1 1-.25 11.4 11.4 0 0 0 3.6.57 1 1 0 0 1 1 1V20a1 1 0 0 1-1 1A17 17 0 0 1 3 4a1 1 0 0 1 1-1h3.5a1 1 0 0 1 1 1c0 1.25.2 2.45.57 3.57a1 1 0 0 1-.25 1z"/></svg>+4791642058</li>
          <li><svg viewBox="0 0 24 24"><path d="M2 5h20v14H2z M2 5l10 8 10-8" stroke="#fff" stroke-width="1.6"/></svg>post@fotovelta.no</li>
          <li><svg viewBox="0 0 24 24"><circle cx="12" cy="12" r="10"/><path d="M2 12h20M12 2c3 3 3 17 0 20M12 2c-3 3-3 17 0 20" stroke="#fff" stroke-width="1.5" fill="none"/></svg>www.fotovelta.no</li>
          <li><svg viewBox="0 0 24 24"><path d="M12 2a7 7 0 0 0-7 7c0 5 7 13 7 13s7-8 7-13a7 7 0 0 0-7-7zm0 9.5A2.5 2.5 0 1 1 12 6.5a2.5 2.5 0 0 1 0 5z"/></svg>Bakkestien22, 6190 Fjordvik</li>
          <li class="social"><span class="dot"></span><span class="dot"></span>FotoVELTA</li>
        </ul>
      </div>
    </div>
  </section>
</main>
</body>
</html>
```